Logo and Card design for KLV Home Solutions LLC

I need an edgier logo and business card designs. Current logo attached. I like the colors below. I would like the logo to incorporate a home in the design.
Title = Principal-Acquisitions
Email:KLVHOMESOLUTIONS@maplenest-mail.com
412-907-2153
facebook
IG
2 sided business card with the front being contact info a slogan about selling a home fast. The back incorporating What we do. Buy houses, land, or commercial property as is. We find solutions to make the process of selling simple and fair.

Target Market(s)

Motivated house sellers.

Industry/Entity Type

Business

Contact Information for Business Card

Who we are: We are a Faith based Real Estate Investment Company. We pay cash for homes in any condition and can close quick. Whatever the reason you need to sell fast, we can help. We believe in creating win-win solutions to help you in your time of need. We care! We can help!

Logo Text

KLV Home Solutions LLC

Font styles to use
Sans Serif

Colors
33a6d7
0355a3
85abd2
cee9f5
9d9d9d
b2b2b2
ffffff

Requirements
Must have
• Old logo attached. I want something edgier.
• Company name, phone number, description on the back of what we can do. Pay all cash. Buy in as is condition. No fees,Commisions or closing costs.Close quick. No hassles with solutions to meet your unique situation.
• Call today for an offer within 24 hours.

```html
<!DOCTYPE html>
<html lang="en">
<head>
<meta charset="utf-8">
<title>KLV Home Solutions LLC – Business Card</title>
<link rel="stylesheet" href="https://fonts.googleapis.com/css2?family=Open+Sans:ital,wght@0,400;0,600;1,400&display=swap">
<style>
  :root {
    --brand-blue: #33a6d7;
    --deep-blue: #0355a3;
    --ink: #1a1a1a;
    --grey: #9d9d9d;
    --paper: #ffffff;
    --pale: #cee9f5;
    --backdrop: #e4e4e4;
  }
  * { margin: 0; padding: 0; box-sizing: border-box; }
  html, body { width: 1200px; height: 900px; overflow: hidden; }
  body {
    background: var(--backdrop);
    font-family: "Open Sans", Arial, sans-serif;
    position: relative;
  }
  .card {
    position: absolute;
    width: 620px;
    height: 350px;
    border-radius: 24px;
    box-shadow: 0 8px 20px rgba(0,0,0,0.2);
    overflow: hidden;
  }

  /* Front: contact side */
  .card-front { left: 40px; top: 470px; background: var(--paper); }
  .contact { position: absolute; left: 40px; top: 30px; }
  .person-name { font-size: 28px; font-weight: 400; color: var(--ink); letter-spacing: -0.5px; line-height: 1.1; }
  .person-title { font-size: 14px; color: var(--brand-blue); margin-top: 2px; }
  .rule { width: 62px; height: 3px; background: var(--brand-blue); margin: 14px 0 12px; }
  .contact-line { display: flex; align-items: center; gap: 8px; font-size: 13px; color: var(--ink); margin-bottom: 6px; }
  .contact-line svg { width: 13px; height: 13px; fill: var(--brand-blue); flex: none; }
  .social { display: flex; align-items: center; gap: 8px; font-size: 13px; color: var(--ink); }
  .social .dot { width: 11px; height: 11px; background: var(--brand-blue); }

  .front-mark { position: absolute; right: 40px; top: 208px; }
  .wordmark { font-size: 22px; font-weight: 600; color: var(--brand-blue); line-height: 1.2; white-space: nowrap; }
  .wordmark-row { display: flex; align-items: center; gap: 10px; }
  .wordmark-row .square { width: 14px; height: 14px; background: var(--brand-blue); flex: none; }
  .offer { position: absolute; right: 70px; bottom: 26px; font-size: 18px; color: var(--brand-blue); }

  /* Back: brand side */
  .card-back { left: 540px; top: 60px; background: var(--brand-blue); }
  .back-inner { position: absolute; inset: 0; display: flex; flex-direction: column; align-items: center; justify-content: center; text-align: center; }
  .back-inner .wordmark { color: var(--paper); font-size: 26px; }
  .back-inner .wordmark-row .square { background: var(--paper); }
  .tagline { font-size: 15px; font-style: italic; color: var(--pale); margin-top: 14px; }
  .services { font-size: 15px; color: var(--pale); margin-top: 10px; }

  /* Standalone brand lockup */
  .brand-lockup { position: absolute; right: 60px; bottom: 50px; }
  .brand-lockup .wordmark { font-size: 28px; }
</style>
</head>
<body>

  <section class="card card-back" aria-label="Card back">
    <div class="back-inner">
      <div class="wordmark-row"><span class="square"></span><span class="wordmark">KLV Home Solutions LLC</span></div>
      <p class="tagline">Your Tagline Here</p>
      <p class="services">Buy houses, land, or commercial property</p>
    </div>
  </section>

  <section class="card card-front" aria-label="Card front">
    <div class="contact">
      <h1 class="person-name">Your Name</h1>
      <p class="person-title">Principal-Acquisitions</p>
      <div class="rule"></div>
      <p class="contact-line">
        <svg viewBox="0 0 24 24" aria-hidden="true"><path d="M6.6 10.8a15 15 0 0 0 6.6 6.6l2.2-2.2a1 1 0 0 1 1-.25 11.4 11.4 0 0 0 3.6.57 1 1 0 0 1 1 1V20a1 1 0 0 1-1 1A17 17 0 0 1 3 4a1 1 0 0 1 1-1h3.5a1 1 0 0 1 1 1c0 1.25.2 2.45.57 3.6a1 1 0 0 1-.25 1z"/></svg>
        412-907-2153
      </p>
      <p class="contact-line">
        <svg viewBox="0 0 24 24" aria-hidden="true"><path d="M2 5h20v14H2z M4 7v.5l8 5 8-5V7l-8 5z" fill-rule="evenodd"/></svg>
        KLVHOMESOLUTIONS@maplenest-mail.com
      </p>
      <p class="contact-line">
        <svg viewBox="0 0 24 24" aria-hidden="true"><path d="M12 2a10 10 0 1 0 0 20 10 10 0 0 0 0-20zm0 2c.9 1.2 1.6 2.6 2 4h-4c.4-1.4 1.1-2.8 2-4zM4.3 14a8 8 0 0 1 0-4h3.4a16 16 0 0 0 0 4zm.8 2h3c.3 1.3.8 2.5 1.4 3.6A8 8 0 0 1 5.1 16zm3-8h-3a8 8 0 0 1 4.4-3.6C8.9 5.5 8.4 6.7 8.1 8zM12 20c-.9-1.2-1.6-2.6-2-4h4c-.4 1.4-1.1 2.8-2 4zm2.3-6H9.7a14 14 0 0 1 0-4h4.6a14 14 0 0 1 0 4zm.2 5.6c.6-1.1 1.1-2.3 1.4-3.6h3a8 8 0 0 1-4.4 3.6zM16.3 14a16 16 0 0 0 0-4h3.4a8 8 0 0 1 0 4zm-.4-6c-.3-1.3-.8-2.5-1.4-3.6A8 8 0 0 1 18.9 8z"/></svg>
        yourwebsite.com
      </p>
      <div class="rule"></div>
      <p class="social"><span class="dot"></span>/Pagebook</p>
    </div>
    <div class="front-mark">
      <div class="wordmark-row"><span class="square"></span><span class="wordmark">KLV Home Solutions LLC</span></div>
    </div>
    <p class="offer">Call today for an offer within 24 hours</p>
  </section>

  <div class="brand-lockup">
    <div class="wordmark-row"><span class="square"></span><span class="wordmark">KLV Home Solutions LLC</span></div>
  </div>

</body>
</html>
```